Business Card Design

Hunting Ranch in the Texas hill country (Deer, Turkey, Quail)

Want Walter on one side and Gloria on the other.
We are looking for a Jack Rabbit NOT a cottontail bunny

Industry/Entity Type

Business

Contact Information for Business Card

Copper Mesa Ranch
Junction Texas
Walter Krimsley Gloria Krimsley
14 Paloverde Hollow Ct. 14 Paloverde Hollow Ct.
The Woodlands, Texas U.S.A. The Woodlands, Texas U.S.A.
281-555-0143 281-555-0187

```html
<!DOCTYPE html>
<html lang="en">
<head>
<meta charset="utf-8">
<title>Copper Mesa Ranch – Business Card</title>
<link rel="stylesheet" href="https://fonts.googleapis.com/css2?family=Montserrat:wght@400;600;700&display=swap">
<style>
  :root {
    --bg: #e9e6e1;
    --paper: #f4f4f4;
    --paper-line: rgba(0,0,0,0.035);
    --ink: #3b3b3b;
    --ink-dark: #333333;
    --band-line: rgba(255,255,255,0.04);
    --light-text: #ffffff;
    --muted-text: #c9c9c9;
    --body-text: #444444;
  }
  * { box-sizing: border-box; margin: 0; padding: 0; }
  html, body {
    width: 1200px; height: 900px; overflow: hidden;
    background: var(--bg);
    font-family: "Montserrat", Arial, sans-serif;
  }
  .stage { position: relative; width: 1200px; height: 900px; }

  .card {
    position: absolute; left: 250px; width: 700px; height: 400px;
    background-color: var(--paper);
    background-image: repeating-linear-gradient(135deg, var(--paper-line) 0 1px, transparent 1px 6px);
    box-shadow: 0 6px 18px rgba(0,0,0,0.18);
    overflow: hidden;
  }
  .card--front { top: 40px; }
  .card--back { top: 470px; }

  /* Front */
  .front__edge-line {
    position: absolute; top: 0; bottom: 0; left: 14px; width: 6px; background: var(--ink);
  }
  .front__band {
    position: absolute; top: 0; bottom: 0; left: 34px; width: 96px;
    background-color: var(--ink);
    background-image: repeating-linear-gradient(135deg, var(--band-line) 0 1px, transparent 1px 6px);
    display: flex; align-items: center; justify-content: center;
  }
  .front__species {
    writing-mode: vertical-rl;
    color: var(--light-text); font-size: 15px; font-weight: 400; letter-spacing: 0.5px;
  }
  .front__brand {
    position: absolute; left: 130px; right: 0; top: 0; bottom: 0;
    display: flex; align-items: center; justify-content: center; gap: 22px;
  }
  .brand-mark {
    width: 64px; height: 64px; border-radius: 50%;
    border: 6px solid var(--ink-dark);
  }
  .brand-name {
    font-size: 34px; font-weight: 700; color: var(--ink-dark);
    letter-spacing: 1px; text-transform: uppercase; line-height: 1.15;
  }

  /* Back */
  .back__band {
    position: absolute; left: 0; right: 0; top: 208px; bottom: 0;
    background-color: var(--ink);
    background-image: repeating-linear-gradient(135deg, var(--band-line) 0 1px, transparent 1px 6px);
  }
  .back__rule {
    position: absolute; left: 0; right: 0; top: 190px; height: 5px; background: var(--ink);
  }
  .back__logo-tile {
    position: absolute; left: 70px; top: 36px; width: 210px; height: 150px;
    background: var(--ink);
    display: flex; flex-direction: column; align-items: center; justify-content: center; gap: 10px;
  }
  .back__logo-tile .brand-mark { width: 44px; height: 44px; border: 4px solid var(--light-text); }
  .back__logo-tile .brand-name { font-size: 18px; color: var(--light-text); text-align: center; }

  .back__address {
    position: absolute; left: 320px; top: 48px;
    display: flex; gap: 12px; align-items: flex-start;
    color: var(--body-text); font-size: 17px; line-height: 1.35;
  }
  .icon-pin { width: 22px; height: 22px; flex: none; margin-top: 1px; }

  .contact {
    position: absolute; top: 268px;
  }
  .contact--walter { left: 70px; }
  .contact--gloria { left: 440px; }
  .contact__name {
    color: var(--light-text); font-size: 24px; font-weight: 700; letter-spacing: 0.5px;
    text-transform: uppercase;
  }
  .contact__phone {
    color: var(--muted-text); font-size: 21px; font-weight: 400; margin-top: 12px; letter-spacing: 1px;
  }
  .icon-phone {
    position: absolute; left: 350px; top: 286px; width: 50px; height: 50px;
  }
</style>
</head>
<body>
<main class="stage">

  <section class="card card--front" aria-label="Card front">
    <div class="front__edge-line"></div>
    <div class="front__band">
      <span class="front__species">Deer, Turkey, Quail</span>
    </div>
    <div class="front__brand">
      <span class="brand-mark" aria-hidden="true"></span>
      <span class="brand-name">Copper Mesa<br>Ranch</span>
    </div>
  </section>

  <section class="card card--back" aria-label="Card back">
    <div class="back__rule"></div>
    <div class="back__band"></div>

    <div class="back__logo-tile">
      <span class="brand-mark" aria-hidden="true"></span>
      <span class="brand-name">Copper Mesa<br>Ranch</span>
    </div>

    <div class="back__address">
      <svg class="icon-pin" viewBox="0 0 22 22" aria-hidden="true">
        <circle cx="11" cy="11" r="10" fill="#3b3b3b"/>
        <path d="M11 5a4 4 0 0 0-4 4c0 3 4 7 4 7s4-4 4-7a4 4 0 0 0-4-4z" fill="#fff"/>
        <circle cx="11" cy="9" r="1.5" fill="#3b3b3b"/>
      </svg>
      <address style="font-style:normal">14 Paloverde Hollow Ct.<br>The Woodlands, Texas U.S.A.</address>
    </div>

    <div class="contact contact--walter">
      <div class="contact__name">Walter Krimsley</div>
      <div class="contact__phone">281-555-0143</div>
    </div>

    <svg class="icon-phone" viewBox="0 0 50 50" aria-hidden="true">
      <circle cx="25" cy="25" r="22" fill="none" stroke="#ffffff" stroke-width="3"/>
      <rect x="18" y="12" width="14" height="26" rx="2" fill="#ffffff"/>
      <rect x="20.5" y="15" width="9" height="8" fill="#3b3b3b"/>
      <g fill="#3b3b3b">
        <rect x="20.5" y="26" width="2" height="2"/><rect x="24" y="26" width="2" height="2"/><rect x="27.5" y="26" width="2" height="2"/>
        <rect x="20.5" y="30" width="2" height="2"/><rect x="24" y="30" width="2" height="2"/><rect x="27.5" y="30" width="2" height="2"/>
        <rect x="20.5" y="34" width="2" height="2"/><rect x="24" y="34" width="2" height="2"/><rect x="27.5" y="34" width="2" height="2"/>
      </g>
    </svg>

    <div class="contact contact--gloria">
      <div class="contact__name">Gloria Krimsley</div>
      <div class="contact__phone">281-555-0187</div>
    </div>
  </section>

</main>
</body>
</html>
```